one page website design - crestloomworks.net

hello.
need a design for crestloomworks.net - small community of developers that create web sites, services and products in cooperation with entrepreneurs for free.
The main condition is that the venture should be a startup. Community has the right to reject the project if they dislike it. Their motivation is to help developing new great services and get share in business. It's a kind of angel investment on seed stage made by developers :)

It should be 1 page scrollable (paralax) website
You can find sections and the text at rough mockup attached. You can pick any colors and style, up to you. Images at mockup should be substituted with other ones (you have the right to use) or with icons. But they have to fit the idea of each section well. The position of the text the way it's placed can be also changed.
Basically anything can be implemented not like in mockup :) It was done just to explain the idea.

Please include simple minimalistic logo.
Design has to be responsive and look well from tablets and smartphones.
Please display how errors have to look line at the form in the bottom. Also result of form submission

Result has to in PSD with versions for tablet and smartphone + logo in separate file in PNG with transparent background.

Target Market(s)

startups, community, venture funding, programming, angel investments

Industry/Entity Type

Community

Number of Pages Required

1 page

Requirements
Must have
• Design has to be responsive and look well from tablets and smartphones.
• Result has to in PSD with versions for tablet and smartphone + logo in separate file in PNG with transparent background.
Should not have
• images that used by many other websites on the web

```html
<!DOCTYPE html>
<html lang="en">
<head>
<meta charset="utf-8">
<title>Crestloom Works – Free Web Development</title>
<link href="https://fonts.googleapis.com/css2?family=Oswald:wght@400;500&family=Roboto:wght@300;400;500&display=swap" rel="stylesheet">
<style>
:root{
  --brand:#1e3f8a;
  --brand-deep:#17357a;
  --steps-a:#2d55a8;
  --steps-b:#21458f;
  --sky:#43a7d4;
  --ink:#1c1c1c;
  --muted:#8a8a8a;
  --form-bg:#efefef;
  --field-line:#d6d6d6;
  --footer:#222324;
  --footer-base:#141414;
  --white:#ffffff;
}
*{box-sizing:border-box;margin:0;padding:0}
html,body{width:1200px;height:2452px;overflow:hidden}
body{font-family:'Roboto',sans-serif;color:var(--ink);background:var(--white);position:relative}
.site-header{position:absolute;top:0;left:0;width:1200px;height:103px;border-top:5px solid var(--brand);background:var(--white)}
.brand-name{position:absolute;left:90px;top:30px;font-family:'Oswald',sans-serif;font-weight:400;font-size:31px;color:var(--brand);letter-spacing:.2px}
.main-nav{position:absolute;right:90px;top:44px;display:flex;gap:48px;font-size:14px;color:#333;font-weight:400}
.hero{position:absolute;top:103px;left:0;width:1200px;height:527px;background:linear-gradient(160deg,#8e949b 0%,#b9bec3 40%,#9aa0a6 70%,#6f747a 100%)}
.hero-title{position:absolute;top:208px;width:100%;text-align:center;font-family:'Oswald',sans-serif;font-size:52px;color:var(--white);font-weight:400}
.hero-sub{position:absolute;top:280px;width:100%;text-align:center;font-family:'Oswald',sans-serif;font-size:31px;line-height:44px;color:var(--white);font-weight:400}
.hero-arrow{position:absolute;top:276px;width:36px;height:36px}
.hero-arrow.prev{left:67px}.hero-arrow.next{right:67px}
.welcome{position:absolute;top:630px;left:0;width:1200px;height:282px;text-align:center}
.welcome h1{margin-top:88px;font-size:28px;font-weight:400;color:var(--ink)}
.welcome h1 span{color:var(--brand)}
.welcome p{width:984px;margin:20px auto 0;font-size:14px;line-height:22px;color:var(--muted)}
.steps{position:absolute;top:912px;left:0;width:1200px;height:445px;background:linear-gradient(135deg,var(--steps-a),var(--steps-b));color:var(--white);text-align:center}
.steps h2{margin-top:59px;font-size:29px;font-weight:400}
.step{position:absolute;top:159px;width:240px;margin-left:-120px}
.step-icon{width:108px;height:108px;border-radius:50%;background:var(--white);margin:0 auto;display:flex;align-items:center;justify-content:center;box-shadow:0 4px 10px rgba(0,0,0,.25)}
.step h3{margin-top:27px;font-size:16px;font-weight:400}
.step p{margin-top:11px;font-size:13px;line-height:19px}
.terms-title{position:absolute;top:1357px;width:1200px;height:126px;text-align:center}
.terms-title h2{margin-top:52px;font-size:29px;font-weight:400}
.terms-panel{position:absolute;top:1483px;height:307px;color:var(--white)}
.terms-panel.agreement{left:0;width:600px;background:var(--sky)}
.terms-panel.preferred{left:600px;width:600px;background:linear-gradient(120deg,#3d4044,#2c2e31)}
.terms-panel h3{position:absolute;top:54px;font-size:24px;font-weight:400}
.terms-panel ul{position:absolute;top:94px;list-style:none;font-size:20px;line-height:35px}
.agreement h3,.agreement ul{left:90px}
.preferred h3,.preferred ul{left:69px}
.terms-panel li::before{content:"»";margin-right:6px}
.apply{position:absolute;top:1790px;left:0;width:1200px;height:357px;background:var(--form-bg)}
.apply h2{position:absolute;top:68px;width:100%;text-align:center;font-size:29px;font-weight:400;color:var(--brand)}
.field{position:absolute;background:var(--white);border:2px solid var(--field-line);font-size:13px;color:#555;padding:0 12px;display:flex;align-items:center}
.field.name{left:90px;top:149px;width:324px;height:59px}
.field.email{left:90px;top:220px;width:324px;height:59px}
.field.idea{left:443px;top:149px;width:324px;height:130px;align-items:flex-start;padding-top:14px}
.btn{position:absolute;font-size:13px;display:flex;align-items:center;justify-content:center}
.btn.choose,.btn.upload{top:149px;width:162px;height:59px;background:linear-gradient(#f7f7f7,#e4e4e4);border:2px solid var(--field-line);color:#555}
.btn.choose{left:788px}.btn.upload{left:948px}
.btn.submit{left:788px;top:220px;width:322px;height:59px;background:linear-gradient(#3a62b0,var(--brand-deep));color:var(--white);font-size:17px;font-weight:500}
.site-footer{position:absolute;top:2147px;left:0;width:1200px;height:237px;background:var(--footer);color:#ddd}
.footer-col{position:absolute;top:45px;font-size:12px;line-height:18px}
.footer-col h4{font-size:16px;font-weight:500;color:var(--white);margin-bottom:18px}
.col-about{left:93px;width:235px}.col-links{left:441px}.col-contact{left:649px;width:220px}.col-news{left:912px;width:210px}
.col-about p{margin-bottom:14px;text-align:justify}
.col-links ul{list-style:none;line-height:24.5px;font-size:11.5px}
.col-links li::before{content:"▸";margin-right:7px;font-size:9px}
.col-contact p{margin-bottom:14px;line-height:24px}
.news-form{display:flex;margin-top:14px;height:30px}
.news-form span{width:140px;background:var(--white);color:#999;font-size:11px;padding:8px 10px}
.news-form b{width:62px;background:var(--brand);color:var(--white);font-weight:400;font-size:12px;display:flex;align-items:center;justify-content:center}
.social{display:flex;gap:17px;margin-top:16px}
.social i{width:32px;height:32px;border:2px solid #ccc;border-radius:50%}
.footer-base{position:absolute;top:2384px;left:0;width:1200px;height:68px;background:var(--footer-base);color:#ddd;font-size:12px;text-align:center;line-height:68px}
</style>
</head>
<body>
<header class="site-header">
  <div class="brand-name">CRESTLOOM WORKS</div>
  <nav class="main-nav"><span>HOW IT WORKS</span><span>TERMS AND PROJECTS</span><span>APPLY</span><span>FORUM</span></nav>
</header>

<section class="hero" role="img" aria-label="Photo of a work desk with laptop, keyboard, camera, coffee cup and tablet">
  <div class="hero-title">FREE WEB DEVELOPMENT</div>
  <div class="hero-sub">We like your idea, we will make all<br>Web development for you for free</div>
  <svg class="hero-arrow prev" viewBox="0 0 36 36"><circle cx="18" cy="18" r="18" fill="#3a3d42"/><path d="M21 11l-7 7 7 7" stroke="#fff" stroke-width="2.5" fill="none"/></svg>
  <svg class="hero-arrow next" viewBox="0 0 36 36"><circle cx="18" cy="18" r="18" fill="#3a3d42"/><path d="M15 11l7 7-7 7" stroke="#fff" stroke-width="2.5" fill="none"/></svg>
</section>

<section class="welcome">
  <h1>WELCOME TO <span>CRESTLOOM WORKS</span></h1>
  <p>Lorem Ipsum has been the industry's standard dummy text ever since the 1500s, when an unknown printer took a galley of type and scrambled it to make a type specimen book. It has survived not only five centuries, but also the leap into electronic typesetting, remaining essentially unchanged. It was popularised in the 1960s with the release of Transmark sheets containing Lorem Ipsum passages, and more recently with desktop publishing</p>
</section>

<section class="steps" role="img" aria-label="Blue-tinted photo of a team working around a table">
  <h2>HOW IT WORKS</h2>
  <div class="step" style="left:219px">
    <div class="step-icon"><svg width="40" height="40" viewBox="0 0 40 40"><path d="M8 6h14v26H8z" fill="var(--brand)"/><path d="M16 12h10l6 6v18H16z" fill="var(--brand)" stroke="#fff" stroke-width="2"/></svg></div>
    <h3>STEP 1</h3><p>you submit idea, brief description,<br>with extended marketing plan</p>
  </div>
  <div class="step" style="left:477px">
    <div class="step-icon"><svg width="40" height="40" viewBox="0 0 40 40"><rect x="5" y="11" width="21" height="18" rx="3" fill="var(--brand)"/><path d="M27 17l9-5v16l-9-5z" fill="var(--brand)"/></svg></div>
    <h3>STEP 2</h3><p>we schedule Linkwave call and<br>discuss it with you</p>
  </div>
  <div class="step" style="left:734px">
    <div class="step-icon"><svg width="44" height="40" viewBox="0 0 44 40"><circle cx="22" cy="13" r="6" fill="var(--brand)"/><circle cx="10" cy="16" r="4.5" fill="var(--brand)"/><circle cx="34" cy="16" r="4.5" fill="var(--brand)"/><path d="M12 32c0-7 4-11 10-11s10 4 10 11z" fill="var(--brand)"/><path d="M2 32c0-5 3-9 8-9 2 0 3 .5 4 1-2 2-3 5-3 8zM42 32c0-5-3-9-8-9-2 0-3 .5-4 1 2 2 3 5 3 8z" fill="var(--brand)"/></svg></div>
    <h3>STEP 3</h3><p>we discuss internally and make<br>decision</p>
  </div>
  <div class="step" style="left:991px">
    <div class="step-icon"><svg width="44" height="40" viewBox="0 0 44 40"><rect x="9" y="9" width="26" height="18" rx="1.5" fill="none" stroke="var(--brand)" stroke-width="3"/><path d="M4 29h36l-2 3H6z" fill="var(--brand)"/></svg></div>
    <h3>STEP 4</h3><p>if our decision is positive<br>we proceed with marketing plan<br>and start the project</p>
  </div>
</section>

<div class="terms-title"><h2>TERMS AND PROJECTS</h2></div>
<section class="terms-panel agreement" role="img" aria-label="Light blue tinted illustration of responsive design sketches">
  <h3>AGREEMENT WE SIGN SUPPOSES THAT</h3>
  <ul><li>we get 40% share in venture</li><li>project is hosted on our servers</li><li>domain belongs to our account</li><li>we are responsible for development</li><li>you are responsible for marketing (sales)</li></ul>
</section>
<section class="terms-panel preferred" role="img" aria-label="Darkened photo of people working in an office">
  <h3>PROJECTS WE PREFER</h3>
  <ul><li>Early proof of concept</li><li>Revenue generation supposed after first version</li><li>b2c service or product</li><li>Advertising based business model</li></ul>
</section>

<section class="apply">
  <h2>APPLY</h2>
  <div class="field name">NAME</div>
  <div class="field email">EMAIL ID</div>
  <div class="field idea">IDEA DESCRIPTION</div>
  <div class="btn choose">CHOOSE FILE</div>
  <div class="btn upload">UPLOAD</div>
  <div class="btn submit">SUBMIT</div>
</section>

<footer class="site-footer">
  <div class="footer-col col-about">
    <h4>CRESTLOOMWORKS</h4>
    <p>Loomhost helps you to quickly and easily build incredible websites with Quillpage.</p>
    <p>Proin gravida nibh vel velit auctor aliquet. Aenean sollicitudin, lorem quis bibendum auctor, nisi elit consequat ipsum, nec sagittis.</p>
  </div>
  <div class="footer-col col-links">
    <h4>LINKS</h4>
    <ul><li>Customer Support</li><li>Documentation</li><li>Resources</li><li>General FAQs</li><li>Shortcodes</li></ul>
  </div>
  <div class="footer-col col-contact">
    <h4>GET IN TOUCH</h4>
    <p>Address : 12 Harrow Lane, Kestrel Quay<br>Avonford, AV3 9QX</p>
    <p>Phone : 555-318-0427</p>
    <p>Email : hello@crestloomworks.net</p>
  </div>
  <div class="footer-col col-news">
    <h4>NEWSLETTER</h4>
    <p>Your about us information would fit here nicely.</p>
    <div class="news-form"><span>Email address</span><b>Submit</b></div>
    <div class="social"><i></i><i></i><i></i></div>
  </div>
</footer>
<div class="footer-base">Copyright © 2016. All Rights Reserved</div>
</body>
</html>
```